Company's Core Values to be on our Office Walls

We are a biotechnology consulting company in Massachusetts with about 40 employees. Please check out velmora.com for our look and more information on our business.

We have 4 core values in the company which we would like to display in our office. (Could be on our walls, could be placed in our website, could be placed anywhere. - We would like a multi-use for this graphic but PRIMARILY on our walls.)
No measurements involved yet, hence we'd like the source file to enable us to stretch the graphics. What's important is to see the designs in this contest.

Design: Looking for a wall display - decal, glass board, vinyl (we're open)
- of our Core Values to have in our reception. We want a Double-Helix
incorporated as the core values are "in our DNA" like the one attached
(would like to see some designs with the exact photo and some used as
inspiration for a unique creative design). Open to various sizes, we have a
few different walls we could place them on.

We are looking for a creative Core Value display to have in our new office. We want a sleek, out of the box design!

Velmora's 4 Core Values are:
> Put Others First
> Have the Courage to Take Action
> Take Personal Responsibility
> Have fun!
***We welcome any infographics per core value. We are open to your creativity!

**WE WANT THE ACTUAL CORE VALUES ON DISPLAY**
We already have a brand (attached).
Need our actual values on display in office.
We want the actual values on the wall, our logo can be incorporated but not
necessarily.

Overview of company: Young consulting firm for biotech and pharmaceuticals
in the Greater Boston area. We are service based, our employees are
engineers and specialists that work on our clients site. Company was
established in 2010, we moved into our New England office 3 months ago!

Colors: Our main color is blue but we also use orange, green, purple, and
teal. See velmora.com for our colors.

Target Market(s)

New Hires and Clients - We want to impress them!
Employees and clients - we want employees inspired by the core
values and clients to be impressed by them/separate us from the competition.

Industry/Entity Type

Biotechnology

Font styles to use
Sans Serif

Colors

Designer to choose colors to be used in the design.

Requirements
Must have
• Creativity!
• Some sort of tie to science/biotech
• Color - Blue is our company color but would like others as well. See website for brand colors.

```html
<!DOCTYPE html>
<html lang="en">
<head>
<meta charset="utf-8">
<title>Velmora Core Values</title>
<link rel="stylesheet" href="https://fonts.googleapis.com/css2?family=Exo+2:wght@700;800&display=swap">
<style>
  :root {
    --ink: #123f5c;
    --paper: #ffffff;
  }
  html, body {
    margin: 0;
    padding: 0;
    width: 1200px;
    height: 1200px;
    overflow: hidden;
    background: var(--paper);
  }
  .core-values {
    position: absolute;
    left: 0;
    top: 279px;
    width: 1200px;
    height: 642px;
  }
  .value-label {
    font-family: "Exo 2", sans-serif;
    font-weight: 800;
    fill: var(--ink);
    letter-spacing: 0.5px;
  }
  .value-label--large { font-size: 36px; }
  .value-label--medium { font-size: 31px; }
  .value-label--end { text-anchor: end; }
  .helix-line, .helix-arc, .helix-node {
    fill: none;
    stroke: var(--ink);
    stroke-width: 2;
  }
  .hub-node {
    fill: none;
    stroke: var(--ink);
    stroke-width: 3;
  }
  .brand-name {
    font-family: "Exo 2", sans-serif;
    font-weight: 800;
    font-size: 19px;
    fill: var(--ink);
    text-anchor: middle;
    letter-spacing: 0.5px;
  }
</style>
</head>
<body>
<svg class="core-values" viewBox="370 1090 710 380" role="group" aria-label="Velmora core values network">
  <!-- connecting lines -->
  <line class="helix-line" x1="704" y1="1203" x2="732" y2="1190"/>
  <line class="helix-line" x1="668" y1="1250" x2="668" y2="1393"/>
  <line class="helix-line" x1="743" y1="1216" x2="743" y2="1201"/>
  <line class="helix-line" x1="741" y1="1230" x2="738" y2="1242"/>
  <line class="helix-line" x1="748" y1="1228" x2="825" y2="1291"/>
  <line class="helix-line" x1="785" y1="1300" x2="823" y2="1297"/>
  <line class="helix-line" x1="829" y1="1303" x2="822" y2="1347"/>
  <line class="helix-line" x1="734" y1="1342" x2="733" y2="1357"/>
  <line class="helix-line" x1="745" y1="1370" x2="790" y2="1371"/>
  <line class="helix-line" x1="723" y1="1376" x2="693" y2="1400"/>

  <!-- value arcs -->
  <path class="helix-arc" d="M 752 1133 A 38 38 0 0 0 786 1202"/>
  <path class="helix-arc" d="M 698 1190 A 38 38 0 0 1 650 1246"/>
  <path class="helix-arc" d="M 795 1402 A 36 36 0 0 1 848 1352"/>
  <path class="helix-arc" d="M 645 1402 A 35 35 0 1 1 668 1463"/>

  <!-- nodes -->
  <circle class="helix-node" cx="743" cy="1223" r="7"/>
  <circle class="helix-node" cx="830" cy="1296" r="7"/>
  <circle class="helix-node" cx="733" cy="1369" r="12"/>

  <!-- central brand hub -->
  <circle class="hub-node" cx="735" cy="1292" r="50"/>
  <text class="brand-name" x="735" y="1299">VELMORA</text>

  <!-- values -->
  <text class="value-label value-label--large" x="757" y="1137">PUT OTHERS</text>
  <text class="value-label value-label--large" x="757" y="1180">FIRST</text>

  <text class="value-label value-label--medium value-label--end" x="686" y="1188">HAVE THE COURAGE</text>
  <text class="value-label value-label--medium value-label--end" x="686" y="1227">TO TAKE ACTION</text>

  <text class="value-label value-label--medium" x="810" y="1387">TAKE PERSONAL</text>
  <text class="value-label value-label--medium" x="810" y="1425">RESPONSIBILITY</text>

  <text class="value-label value-label--medium value-label--end" x="683" y="1440">HAVE FUN!</text>
</svg>
</body>
</html>
```